Jewelry Business card for general purpose. Elegant and simple

We are a jewelry group with 6 stores in Mexico and 30 years in business.

We need a BC that at leats includes the name, mail, phone number and physical location (street, municipality, and county; example "Paseo Arboleda 2140", "Avenida Quelites", "Monterrey").
Optional: we are trying to reposition the brand with the association of life-events or moments and family. Such as: birth, marriage, graduation, birthdays. Christmast, mothers day and fathers day.

We are looking for something elegant but simple

Jewelry name: "Lumora". Email: "lumoradesa@velmino.com". Phone num "4172-6395".

Target Market(s)

General business card: from suppliers to clients. One segment outstand: couples gettineg married

Industry/Entity Type

Jewelry Store

Contact Information for Business Card

Loking for something simple but elegant.

Font styles to use
Decorative
Script

Requirements
Must have
• Must have name, address, and mail.
Nice to have
• It could have jewelry pictures/design. Maybe quotes. Or general words as background . currently we have a very simple card with one ring would like to see something different.
Should not have
• Include real people.

```html
<!DOCTYPE html>
<html lang="es">
<head>
<meta charset="utf-8">
<title>Joyeria Lumora – Tarjeta de presentación</title>
<link rel="stylesheet" href="https://fonts.googleapis.com/css2?family=Marck+Script&family=Open+Sans:wght@400&display=swap">
<style>
  :root {
    --page-bg: #ece7e1;
    --card-light: #cfa377;
    --card-mid: #b98a5d;
    --card-dark: #a67650;
    --ink-dark: #1c1410;
    --ink-light: #fbf4ec;
    --rule: #f4ece4;
    --gold-light: #f3e3a6;
    --gold-mid: #d9bd72;
    --gold-dark: #a98a45;
  }
  html, body {
    margin: 0;
    width: 1200px;
    height: 1022px;
    overflow: hidden;
    background: var(--page-bg);
  }
  .canvas {
    position: relative;
    width: 1200px;
    height: 1022px;
  }
  .business-card {
    position: absolute;
    left: 150px;
    top: 251px;
    width: 900px;
    height: 520px;
    border-radius: 14px;
    overflow: hidden;
    background: linear-gradient(200deg, var(--card-light) 0%, var(--card-mid) 55%, var(--card-dark) 100%);
    box-shadow: 0 18px 40px rgba(60, 40, 20, 0.25);
  }
  .emblem-watermark {
    position: absolute;
    left: 560px;
    top: 120px;
    width: 280px;
    height: 250px;
    border-radius: 50%;
    background: radial-gradient(ellipse at center, rgba(240, 215, 180, 0.35) 0%, rgba(240, 215, 180, 0.12) 55%, rgba(240, 215, 180, 0) 75%);
  }
  .title-rule {
    position: absolute;
    left: 70px;
    top: 108px;
    width: 330px;
    height: 2px;
    background: var(--rule);
  }
  .brand-name {
    position: absolute;
    right: 70px;
    top: 38px;
    margin: 0;
    font-family: "Marck Script", cursive;
    font-weight: 400;
    font-size: 64px;
    line-height: 1;
    color: var(--ink-dark);
  }
  .address,
  .contact {
    position: absolute;
    right: 60px;
    margin: 0;
    font-family: "Open Sans", sans-serif;
    font-style: normal;
    font-size: 20px;
    line-height: 1.45;
    color: var(--ink-light);
    text-align: right;
    letter-spacing: 0.5px;
  }
  .address { top: 160px; }
  .contact { top: 268px; line-height: 1.9; }
  .contact-line {
    display: flex;
    justify-content: flex-end;
    align-items: center;
    gap: 10px;
  }
  .contact-line svg { width: 16px; height: 16px; }
  .jewel-photo {
    position: absolute;
    left: 85px;
    top: 285px;
    width: 400px;
    height: 185px;
    border-radius: 50% / 45%;
    background: radial-gradient(ellipse at 45% 35%, var(--gold-light) 0%, var(--gold-mid) 55%, var(--gold-dark) 100%);
  }
  .edge-stripe {
    position: absolute;
    left: 0;
    right: 0;
    bottom: 16px;
    height: 3px;
    background: var(--rule);
  }
</style>
</head>
<body>
<main class="canvas">
  <article class="business-card">
    <div class="emblem-watermark" role="img" aria-label="Faint decorative swirl of a jewelled ring behind the contact details"></div>
    <div class="title-rule"></div>
    <h1 class="brand-name">Joyeria Lumora</h1>
    <address class="address">
      Paseo Arboleda 2140,<br>
      Avenida Quelites, Monterrey
    </address>
    <div class="contact">
      <div class="contact-line">
        <span>4172-6395</span>
        <svg viewBox="0 0 16 16" aria-hidden="true"><path d="M4 2c1 0 2 2.5 2 3s-1 1-1 1.5 2 4 4.5 4.5c.5 0 1-1 1.5-1s3 1 3 2-1 2-2 2C7 14 2 9 2 4c0-1 1-2 2-2z" fill="var(--ink-light)"/></svg>
      </div>
      <div class="contact-line">
        <span>lumoradesa@velmino.com</span>
        <svg viewBox="0 0 16 16" aria-hidden="true"><rect x="1.5" y="3.5" width="13" height="9" fill="none" stroke="var(--ink-light)" stroke-width="1.5"/><path d="M1.5 3.5 8 9l6.5-5.5" fill="none" stroke="var(--ink-light)" stroke-width="1.5"/></svg>
      </div>
    </div>
    <div class="jewel-photo" role="img" aria-label="Photograph of a gold ring set with a spiral of diamonds"></div>
    <div class="edge-stripe"></div>
  </article>
</main>
</body>
</html>
```